Hi, Looking for an upgraded business card to the aged one attached. Open to suggestions and no real limitations, but if your going to use a picture of a taxi i think it should be vector based rather than a full color picture. I've uploaded a 2 pictures of the type of taxi which is a Torvane K5 in white. The taxi markings look like the pink one in the picture but to be clear his is white. The taxi is in Bermuda so if you wanted to include something island based that's ok as well but not required. The other thing he wanted to keep on there was the Harbour Constabulary, with the retired police office incorporated somehow.

Requirements
Must have
• Bermuda Taxi Operator
Retired Police Officer
Police Crest
Taxi #
Email
Mobile Number

```html
<!DOCTYPE html>
<html lang="en">
<head>
<meta charset="utf-8">
<title>Bermuda Taxi Operator – Business Cards</title>
<link rel="stylesheet" href="https://fonts.googleapis.com/css2?family=Arimo:wght@700&family=Roboto:wght@400;500;700&display=swap">
<style>
  :root {
    --navy: #174a7c;
    --navy-deep: #12467f;
    --band-tone: #8ea6c0;
    --white: #ffffff;
    --stage: #3a2c24;
    --silver-light: #eef0f2;
    --silver-dark: #9ea3a8;
    --pink-light: #f59ac8;
    --pink-dark: #d94a93;
  }
  * { box-sizing: border-box; margin: 0; padding: 0; }
  html, body {
    width: 1200px;
    height: 1200px;
    overflow: hidden;
    background: var(--stage);
  }
  .sheet { position: relative; width: 1200px; height: 1200px; }
  .card {
    position: absolute;
    left: 234px;
    width: 734px;
    height: 418px;
    border-radius: 26px;
    overflow: hidden;
    background: var(--white);
    font-family: "Roboto", sans-serif;
  }
  .card--white-van { top: 176px; }
  .card--pink-van { top: 642px; }

  .crest-mark {
    position: absolute;
    left: 64px;
    top: 52px;
    width: 170px;
    display: flex;
    flex-direction: column;
    align-items: center;
    gap: 10px;
  }
  .crest-mark__dot {
    width: 62px;
    height: 62px;
    border-radius: 50%;
    background: var(--navy);
  }
  .crest-mark__name {
    font-family: "Roboto", sans-serif;
    font-weight: 700;
    font-size: 16px;
    line-height: 1.2;
    color: var(--navy);
    text-align: center;
  }

  .title {
    position: absolute;
    left: 248px;
    top: 92px;
    font-family: "Arimo", sans-serif;
    font-weight: 700;
    font-size: 34px;
    color: var(--navy);
    white-space: nowrap;
  }

  .pattern-band {
    position: absolute;
    left: 0;
    top: 228px;
    width: 100%;
    height: 22px;
    background: linear-gradient(180deg, #c3d0de, var(--band-tone));
  }
  .info-panel {
    position: absolute;
    left: 0;
    top: 250px;
    width: 100%;
    height: 168px;
    background: var(--navy-deep);
  }

  .vehicle {
    position: absolute;
    border-radius: 30px 60px 18px 18px;
  }
  .vehicle--white {
    left: 232px;
    top: 158px;
    width: 272px;
    height: 122px;
    background: linear-gradient(180deg, var(--silver-light), var(--silver-dark));
  }
  .vehicle--pink {
    left: 224px;
    top: 146px;
    width: 290px;
    height: 150px;
    background: linear-gradient(180deg, var(--pink-light), var(--pink-dark));
  }

  .owner-name, .owner-role, .email, .taxi-number, .phone {
    position: absolute;
    color: var(--white);
    white-space: nowrap;
  }
  .owner-name { left: 56px; top: 280px; font-size: 23px; font-weight: 700; }
  .owner-role { left: 56px; top: 314px; font-size: 24px; font-weight: 400; }
  .email {
    left: 20px; top: 364px; font-size: 24px; font-weight: 400;
    display: flex; align-items: center; gap: 14px;
  }
  .email svg { width: 22px; height: 22px; }
  .divider {
    position: absolute;
    left: 366px;
    top: 306px;
    height: 60px;
    border-left: 5px dotted var(--white);
  }
  .taxi-number { left: 434px; top: 318px; font-size: 25px; font-weight: 400; }
  .phone {
    left: 388px; top: 352px; font-size: 33px; font-weight: 700;
    display: flex; align-items: center; gap: 6px;
  }
  .phone svg { width: 22px; height: 22px; }
</style>
</head>
<body>
<main class="sheet">

  <article class="card card--white-van">
    <div class="crest-mark">
      <span class="crest-mark__dot"></span>
      <span class="crest-mark__name">Harbour Constabulary</span>
    </div>
    <h1 class="title">Bermuda Taxi Operator</h1>
    <div class="pattern-band" role="img" aria-label="Checkered police band pattern"></div>
    <div class="info-panel"></div>
    <div class="vehicle vehicle--white" role="img" aria-label="Photo of a white Torvane K5 passenger van"></div>
    <p class="owner-name">Marcus Tavell</p>
    <p class="owner-role">Retired Police Officer</p>
    <p class="email">
      <svg viewBox="0 0 24 24" aria-hidden="true"><path fill="#fff" d="M2 9l10-6 10 6v12H2z"/><path fill="none" stroke="#12467f" stroke-width="1.8" d="M3 10l9 6 9-6"/></svg>
      mtavell208@mailbox.com
    </p>
    <span class="divider"></span>
    <p class="taxi-number">Taxi # T2471</p>
    <p class="phone">
      <svg viewBox="0 0 24 24" aria-hidden="true"><path fill="#fff" d="M6.6 2.5l3 3.2-1.8 2.6c1 2.4 3.5 5 6 6l2.6-1.8 3.2 3-1.6 3.6C10.6 19.1 4.9 13.4 3 5.6z"/></svg>
      1-555-014-2276
    </p>
  </article>

  <article class="card card--pink-van">
    <div class="crest-mark">
      <span class="crest-mark__dot"></span>
      <span class="crest-mark__name">Harbour Constabulary</span>
    </div>
    <h1 class="title">Bermuda Taxi Operator</h1>
    <div class="pattern-band" role="img" aria-label="Checkered police band pattern"></div>
    <div class="info-panel"></div>
    <div class="vehicle vehicle--pink" role="img" aria-label="Photo of a pink Torvane K5 taxi van with roof sign"></div>
    <p class="owner-name">Marcus Tavell</p>
    <p class="owner-role">Retired Police Officer</p>
    <p class="email">
      <svg viewBox="0 0 24 24" aria-hidden="true"><path fill="#fff" d="M2 9l10-6 10 6v12H2z"/><path fill="none" stroke="#12467f" stroke-width="1.8" d="M3 10l9 6 9-6"/></svg>
      mtavell208@mailbox.com
    </p>
    <span class="divider"></span>
    <p class="taxi-number">Taxi # T2471</p>
    <p class="phone">
      <svg viewBox="0 0 24 24" aria-hidden="true"><path fill="#fff" d="M6.6 2.5l3 3.2-1.8 2.6c1 2.4 3.5 5 6 6l2.6-1.8 3.2 3-1.6 3.6C10.6 19.1 4.9 13.4 3 5.6z"/></svg>
      1-555-014-2276
    </p>
  </article>

</main>
</body>
</html>
```